film festival poster

We need a poster designed for our film festival. It is called the Open Horizon Cinema Gathering www.openhorizoncinema.example This is a film festival about what it means to be free. We want the image to be bold and different, and yet speak about film and the importance of being a free human being. Maybe a combination of images that make up a bigger image?

```html
<!DOCTYPE html>
<html lang="en">
<head>
<meta charset="utf-8">
<title>Open Horizon Cinema Gathering – Poster</title>
<link rel="stylesheet" href="https://fonts.googleapis.com/css2?family=Source+Sans+3:wght@400;700;900&display=swap">
<style>
  :root {
    --ink: #231f20;
    --paper: #ffffff;
    --crimson: #c21a4a;
    --crimson-deep: #8e1236;
    --reel: #2b2829;
    --reel-light: #9a9a9a;
  }
  * { margin: 0; padding: 0; box-sizing: border-box; }
  html, body {
    width: 857px; height: 1200px; overflow: hidden;
    background: var(--ink);
  }
  .poster {
    position: relative; width: 857px; height: 1200px; overflow: hidden;
    background: var(--ink);
    font-family: "Source Sans 3", "Myriad Pro", Arial, sans-serif;
    color: var(--ink);
  }
  .projector-beam { position: absolute; inset: 0; }
  .origami-bird {
    position: absolute; left: 86px; top: 55px; width: 484px; height: 374px;
    background: radial-gradient(ellipse at 50% 50%, var(--crimson) 0%, var(--crimson-deep) 45%, rgba(142,18,54,0) 72%);
  }
  .film-reel {
    position: absolute; left: 693px; top: 455px; width: 304px; height: 304px;
    border-radius: 50%;
    background: radial-gradient(circle at 40% 50%, var(--reel-light) 0%, var(--reel) 60%);
  }
  .festival-name {
    position: absolute; left: 108px; top: 568px;
    font-weight: 900; font-size: 92px; line-height: 1; letter-spacing: -2px;
    white-space: nowrap;
  }
  .festival-type {
    position: absolute; left: 110px; top: 688px;
    font-weight: 400; font-size: 51px; line-height: 1; letter-spacing: 0.5px;
    text-transform: uppercase; white-space: nowrap;
  }
  .festival-dates {
    position: absolute; left: 112px; top: 772px;
    font-weight: 700; font-size: 32px; line-height: 1; white-space: nowrap;
  }
  .festival-venue {
    position: absolute; left: 112px; top: 812px;
    font-weight: 400; font-size: 32px; line-height: 1; white-space: nowrap;
  }
  .contact {
    position: absolute; left: 0; right: 0; top: 1108px;
    text-align: center; color: var(--paper);
  }
  .contact-web { font-weight: 700; font-size: 29px; line-height: 1.2; }
  .contact-social {
    display: flex; justify-content: center; align-items: center; gap: 8px;
    margin-top: 8px; font-weight: 700; font-size: 22px; line-height: 1;
  }
  .social-mark { width: 18px; height: 18px; background: var(--paper); }
  .social-name { margin-right: 6px; font-size: 16px; }
</style>
</head>
<body>
<main class="poster">
  <svg class="projector-beam" width="857" height="1200" viewBox="0 0 857 1200" aria-hidden="true">
    <polygon points="0,138 857,422 857,766 0,973" fill="var(--paper)"/>
  </svg>

  <div class="origami-bird" role="img" aria-label="Crimson folded-paper bird flying upward"></div>
  <div class="film-reel" role="img" aria-label="Film reel at the source of the projector beam"></div>

  <h1 class="festival-name">Open Horizon</h1>
  <p class="festival-type">Cinema Gathering</p>
  <p class="festival-dates">April 8, 9 &amp; 10</p>
  <p class="festival-venue">Harbour Lights, Eastfield</p>

  <footer class="contact">
    <p class="contact-web">http://www.openhorizoncinema.example</p>
    <p class="contact-social">
      <span class="social-mark"></span>
      <span class="social-name">Gatherly</span>
      <span>www.gatherly.example/OpenHorizonCinema</span>
    </p>
  </footer>
</main>
</body>
</html>
```